Product label for herbal salves, lotions, soaps and tinctures

We need a very simple, clean and organic looking label that can be used for an ointment jar, a lotion bottle and a dropper bottle.
We have an existing logo (see attached). We like the colors white, olive green, gold and black. It needs to include product name as dominant and logo. It also needs to include an ingredient list, and usage statement. Include weight of product, distributed by, made in the USA, and NQB statement.
Example of what needs to be present:
Logo
Name: Calmwick Balm
Used for: For Muscle Aches, Arthritis, Tendonitis, Headaches
To Use: For muscle aches, arthritis and tendonitis, massage into affected area. For tension headache apply to neck, temples and forehead.
Store in a cool and dry place, away from direct heat and sunlight.
Weight of product: 1.75
DIST. BY: Brookmere Herbal
Made in the USA
This product is not intended to diagnose, treat, cure
or prevent any disease. Not regulated
by the NQB. Please consult your health care practitioner
before using product. Discontinue use if any adverse reaction occurs.
Ingredient list:
Wildcrafted Ingredients:
Ashwagandha Root, Peppermint Leaf, Hops Flowers, St. John’s Wort Herb, Arnica Flowers, Green Tea Leaf, Alfalfa Leaf, Dandelion Root, Burdock Root, Chickweed Herb, Chaparral Leaf, Yarrow Flowers, Boneset Herb, Moringa Leaf, Meadowsweet Herb, Nettle Leaf
Organic Ingredients:
Olive Oil, Aloe Leaf, Sweet Birch Bark, Helichrysum Flowers, Holy Basil Leaf, Borage Herb, Ginger Root, Angelica Root, White Willow Bark, Mustard Seed, Beeswax, Vitamin E, Essential Oils
Dimensions of Jar:
Circumference: 7 in.
Height: 1 in.

```html
<!DOCTYPE html>
<html lang="en">
<head>
<meta charset="utf-8">
<title>Brookmere Herbal – Calmwick Balm Label</title>
<link href="https://fonts.googleapis.com/css2?family=Open+Sans:wght@400;600;700&display=swap" rel="stylesheet">
<style>
  :root {
    --olive: #5f6b1f;
    --olive-light: #8a9440;
    --gold: #c98f2a;
    --green: #6db33f;
    --black: #111111;
    --ink: #1e1e1e;
    --white: #ffffff;
    --backdrop: #d6d7db;
  }
  * { box-sizing: border-box; margin: 0; padding: 0; }
  html, body { width: 1200px; height: 672px; overflow: hidden; }
  body {
    background: var(--backdrop);
    font-family: "Open Sans", Arial, sans-serif;
    color: var(--ink);
    position: relative;
  }
  .label {
    position: absolute;
    left: 0; top: 246px;
    width: 1200px; height: 180px;
    background: var(--white);
  }
  .label__rule {
    position: absolute; left: 0; width: 1200px; height: 3px;
    background: linear-gradient(90deg, transparent 0%, var(--green) 12%, var(--green) 88%, transparent 100%);
  }
  .label__rule--top { top: 6px; }
  .label__rule--bottom { bottom: 6px; }

  /* Ingredients */
  .ingredients { position: absolute; left: 40px; top: 22px; width: 352px; }
  .ingredients__title { color: var(--olive); font-size: 14px; font-weight: 600; margin-bottom: 4px; }
  .ingredients__group {
    background: var(--gold); color: var(--white);
    font-size: 9.5px; font-weight: 700; padding: 1px 4px; margin-bottom: 3px;
  }
  .ingredients__list { font-size: 6.6px; line-height: 14px; margin-bottom: 5px; font-weight: 600; }

  /* Brand block */
  .brand { position: absolute; left: 490px; top: 18px; width: 230px; text-align: center; }
  .brand__name {
    display: flex; align-items: center; justify-content: center; gap: 6px;
    color: var(--olive); font-size: 24px; font-weight: 700; line-height: 1;
    height: 66px;
  }
  .brand__dot { width: 12px; height: 12px; border-radius: 50%; background: var(--olive); }
  .product-name { position: relative; width: 224px; height: 34px; margin: 0 auto; }
  .product-name svg { position: absolute; inset: 0; }
  .product-name__text {
    position: absolute; inset: 0; display: flex; align-items: center; justify-content: center;
    color: var(--gold); font-size: 14px; font-weight: 700; letter-spacing: .3px;
  }
  .weight {
    display: inline-block; margin-top: 6px;
    background: var(--green); color: var(--white);
    font-size: 14px; width: 96px; height: 24px; line-height: 24px;
    border-radius: 3px 3px 0 0;
  }

  /* Usage */
  .usage { position: absolute; left: 810px; top: 22px; width: 282px; font-size: 7px; line-height: 1.35; }
  .usage__key { color: var(--olive); font-size: 10px; font-weight: 600; }
  .usage p { margin-bottom: 6px; }
  .usage__consult {
    display: inline-block; background: var(--gold); color: var(--white);
    font-size: 7.5px; padding: 3px 6px; margin-bottom: 4px;
  }

  .distributor {
    position: absolute; left: 1110px; top: 34px; width: 40px; height: 120px;
    display: flex; align-items: center; justify-content: center;
  }
  .distributor__text {
    transform: rotate(90deg); white-space: nowrap;
    font-size: 9px; font-weight: 700; line-height: 1.3; text-align: left;
  }
</style>
</head>
<body>
  <section class="label">
    <div class="label__rule label__rule--top"></div>

    <div class="ingredients">
      <h2 class="ingredients__title">Ingredient list:</h2>
      <div class="ingredients__group">Wildcrafted Ingredients:</div>
      <p class="ingredients__list">Ashwagandha Root, Peppermint Leaf, Hops Flowers, St. John’s Wort Herb, Arnica Flowers, Green Tea Leaf, Alfalfa Leaf, Dandelion Root, Burdock Root, Chickweed Herb, Chaparral Leaf, Yarrow Flowers, Boneset Herb, Moringa Leaf, Meadowsweet Herb, Nettle Leaf</p>
      <div class="ingredients__group">Organic Ingredients:</div>
      <p class="ingredients__list">Olive Oil, Aloe Leaf, Sweet Birch Bark, Helichrysum Flowers, Holy Basil Leaf, Borage Herb, Ginger Root, Angelica Root, White Willow Bark, Mustard Seed, Beeswax, Vitamin E, Essential Oils</p>
    </div>

    <div class="brand">
      <div class="brand__name"><span class="brand__dot"></span>Brookmere Herbal</div>
      <div class="product-name">
        <svg width="224" height="34" viewBox="0 0 224 34">
          <path d="M6 34 C10 12 22 2 46 2 L224 2 C220 18 212 30 196 34 Z" fill="var(--olive-light)"/>
          <path d="M0 34 C4 14 16 4 38 4 L216 4 C212 20 204 32 188 34 Z" fill="var(--black)"/>
        </svg>
        <div class="product-name__text">CALMWICK BALM</div>
      </div>
      <span class="weight">1.75g</span>
    </div>

    <div class="usage">
      <p><span class="usage__key">Used for:</span> For Muscle Aches, Arthritis, Tendonitis, Headaches<br>
      <span class="usage__key">To Use:</span> For muscle aches, arthritis and tendonitis, massage into affected area. For tension headache apply to neck, temples and forehead.</p>
      <p>Store in a cool and dry place, away from direct heat and sunlight.</p>
      <p>This product is not intended to diagnose, treat, cure or prevent any disease.<br>Not regulated by the NQB.</p>
      <span class="usage__consult">Please consult your health care practitioner</span>
      <p>Before using product. Discontinue use if any adverse reaction occurs.</p>
    </div>

    <div class="distributor">
      <div class="distributor__text">DIST. BY: Brookmere Herbal<br>Made in the USA</div>
    </div>

    <div class="label__rule label__rule--bottom"></div>
  </section>
</body>
</html>
```